Health Coach needs a Business Card Design

Need a really modern feminine business card design for a health and lifestyle coach. Needs to use geometric shapes, muted grey/blue/green pastels and black and white - see mood board attached and logo. The client likes black and white, modern, san serif with the use of lines and possibly a shadow leaf as in the mood board. Possibly put the tag line on the back or an icon of the logo. Logo is also attached. An icon of the logo would be great too.

Target Market(s)

Women (some men) aged 30 to 50.

Industry/Entity Type

Business

Contact Information for Business Card

Marla Teveny
e-mail: hello@marlatwell.example
website: marlatwell.example
Phone: +610497258316

The tag line is "Calm strength every day"

Font styles to use
Sans Serif

Colors
ecf7fb
cfeae6
000000
ffffff
f5f5f5

Requirements
Must have
• Black and white, logo, tag line and details
Nice to have
• Would be nice to incorporate the shadow palm.fern leaves as in the mood board and or geometric lines/shapes - see mood board. Could be either standard rectangle or would be happy with square too.
Should not have
• Flowers or decorations

```html
<!DOCTYPE html>
<html lang="en">
<head>
<meta charset="utf-8">
<title>Marla Wellness — Business Card</title>
<link rel="stylesheet" href="https://fonts.googleapis.com/css2?family=Open+Sans:ital,wght@0,300;0,400;0,600;1,600&display=swap">
<style>
  :root {
    --bg: #f5f5f5;
    --mint: #cfeae6;
    --charcoal: #363636;
    --ink: #000000;
    --white: #ffffff;
    --rule: #8a8a8a;
  }
  html, body {
    margin: 0;
    padding: 0;
    overflow: hidden;
  }
  .canvas {
    position: relative;
    width: 1200px;
    height: 900px;
    background: var(--bg);
    overflow: hidden;
  }
  .card {
    position: absolute;
    border-radius: 22px;
    overflow: hidden;
    background: var(--charcoal);
    box-shadow: 0 6px 18px rgba(0,0,0,0.12);
  }
  .card--front {
    left: 252px;
    top: 60px;
    width: 556px;
    height: 345px;
  }
  .card--back {
    left: 458px;
    top: 518px;
    width: 559px;
    height: 344px;
  }
  .front-band {
    position: absolute;
    left: 0; top: 0;
    width: 100%;
    height: 143px;
    background: var(--mint);
  }
  .brand {
    position: absolute;
    left: 0;
    width: 100%;
    text-align: center;
    font-family: "Open Sans", sans-serif;
  }
  .brand-name {
    font-weight: 300;
    font-size: 32px;
    letter-spacing: 1px;
    line-height: 1;
  }
  .tagline {
    font-weight: 400;
    font-size: 11px;
    letter-spacing: 2.4px;
    line-height: 1;
    margin-top: 12px;
    text-transform: uppercase;
  }
  .card--front .brand { top: 48px; color: var(--ink); }
  .card--back .brand { top: 146px; color: var(--white); }
  .details {
    position: absolute;
    top: 207px;
    left: 0;
    width: 100%;
    text-align: center;
    color: var(--white);
    font-family: "Open Sans", sans-serif;
  }
  .person-name {
    font-style: italic;
    font-weight: 600;
    font-size: 21px;
    margin: 0;
    line-height: 1;
  }
  .name-rule {
    width: 190px;
    height: 1px;
    background: var(--rule);
    margin: 14px auto 12px;
  }
  .contact {
    font-size: 14px;
    line-height: 22px;
    margin: 0;
  }
  .contact b { font-weight: 600; }
  .sep {
    display: inline-block;
    width: 1.5px;
    height: 17px;
    background: var(--white);
    vertical-align: -3px;
    margin: 0 4px;
  }
</style>
</head>
<body>
<main class="canvas">
  <section class="card card--front" aria-label="Business card front">
    <div class="front-band"></div>
    <div class="brand">
      <div class="brand-name">Marla Wellness</div>
      <div class="tagline">Calm strength every day</div>
    </div>
    <div class="details">
      <p class="person-name">Marla Teveny</p>
      <div class="name-rule"></div>
      <p class="contact"><b>P:</b> +610497258316<span class="sep"></span><b>E:</b> hello@marlatwell.example</p>
      <p class="contact">www.marlatwell.example</p>
    </div>
  </section>

  <section class="card card--back" aria-label="Business card back">
    <div class="brand">
      <div class="brand-name">Marla Wellness</div>
      <div class="tagline">Calm strength every day</div>
    </div>
  </section>
</main>
</body>
</html>
```